Need new look for home page of Makeup Artist Site

We want a new, clean, modern, professional look for the new design for our website. Our current site is at https://glowvra.com. We would like a high fashion site with diverse ethnic groups represented throughout the page. We like trelk.com as an example of style and user experience. This website is for people to look for a makeup artist or esthetician to come to their home and perform a service there. They will pay on the website and be able to review available service providers and choose one. We will need 2 additional pages once this design is approved. We will pay separately for those.

```html
<!DOCTYPE html>
<html lang="en">
<head>
<meta charset="utf-8">
<title>GLOWVRA — Make Up &amp; Facial Care at Home</title>
<link rel="stylesheet" href="https://fonts.googleapis.com/css2?family=Poppins:ital,wght@0,300;0,400;0,500;0,600;0,700;1,300;1,400&display=swap">
<style>
:root{
  --red:#e32636;
  --red-bright:#ef2b2b;
  --ink:#1e1e1e;
  --white:#ffffff;
  --quote-bg:#e6e6e6;
  --quote-ink:#555555;
  --testimonial-bg:#333333;
  --footer-bg:#1c1c1c;
  --footer-link:#c9c9c9;
}
*{margin:0;padding:0;box-sizing:border-box}
html,body{width:1200px;height:3002px;overflow:hidden}
body{font-family:'Poppins',sans-serif;color:var(--ink);position:relative;background:var(--white)}
a{color:inherit;text-decoration:none}
.section{position:absolute;left:0;width:1200px;overflow:hidden}
.photo{position:absolute;inset:0}

/* header */
.site-header{position:absolute;top:0;left:0;width:1200px;height:90px;z-index:5}
.brand{position:absolute;left:90px;top:30px;font-size:34px;font-weight:700;letter-spacing:1px;color:var(--ink)}
.main-nav{position:absolute;top:36px;left:681px;display:flex;gap:23px;font-size:11px;font-weight:600;letter-spacing:1px}
.main-nav a.active{color:var(--red-bright)}
.btn-started{position:absolute;left:983px;top:29px;width:121px;height:27px;background:var(--red-bright);color:var(--white);font-size:11px;font-weight:600;letter-spacing:1px;display:flex;align-items:center;justify-content:center}

/* hero */
.hero{top:0;height:644px}
.hero .photo{background:linear-gradient(100deg,#eeebe8 0%,#ebe6e2 45%,#e7d8cf 70%,#e9e4e0 100%)}
.hero-title{position:absolute;left:142px;top:234px;font-size:37px;font-weight:500;line-height:43px}
.hero-title em{font-style:normal;color:var(--red-bright)}
.btn-signin{position:absolute;left:143px;top:365px;width:158px;height:46px;background:var(--red-bright);color:var(--white);font-size:15px;font-weight:600;letter-spacing:1.5px;display:flex;align-items:center;justify-content:center}
.slider-arrow{position:absolute;top:263px}

/* feature bands */
.feature{color:var(--white)}
.feature h2{font-size:35px;font-weight:600;letter-spacing:.5px;line-height:1}
.feature p{font-size:17px;font-style:italic;font-weight:300;line-height:24.5px;margin-top:24px}
.feature .more{display:inline-flex;align-items:center;gap:8px;font-size:16px;font-weight:500;margin-top:36px}
.esthetician{top:644px;height:501px}
.esthetician .photo{background:linear-gradient(90deg,#5a1f25 0%,#c2344a 22%,#9a5a60 42%,#8a7a78 60%,#7e7a77 100%)}
.esthetician .copy{position:absolute;right:98px;top:113px;text-align:right;width:520px}
.makeup{top:1145px;height:510px}
.makeup .photo{background:linear-gradient(90deg,#5e6785 0%,#616a88 55%,#9096a6 70%,#d9c8c2 85%,#e4d3cd 100%)}
.makeup .copy{position:absolute;left:142px;top:122px;width:560px}

/* quote */
.quote{top:1655px;height:147px;background:var(--quote-bg);text-align:center;color:var(--quote-ink);font-style:italic;font-size:17px}
.quote blockquote{position:absolute;left:0;top:48px;width:100%}
.quote cite{display:block;position:absolute;left:0;top:83px;width:100%;font-style:italic}

/* about */
.about{top:1802px;height:465px;background:var(--red);color:var(--white)}
.about h2{position:absolute;left:0;top:62px;width:100%;text-align:center;font-size:31px;font-weight:700}
.about-col{position:absolute;top:184px;width:335px}
.about-col h3{font-size:20px;font-weight:600;margin-bottom:8px}
.about-col p{font-size:13.3px;line-height:21px;font-weight:400}

/* cta cards */
.cta{top:2267px;height:268px}
.cta-card{position:absolute;top:0;width:600px;height:268px;color:var(--white)}
.cta-card .photo{inset:0}
.cta-red .photo{background:linear-gradient(100deg,#c8141f 0%,#dc2027 50%,#e4847c 80%,#d44a48 100%)}
.cta-blue .photo{background:linear-gradient(100deg,#9aa4bf 0%,#8e98b4 50%,#c9c4c8 80%,#5a5352 100%)}
.cta-card a{position:absolute;top:172px;display:flex;align-items:center;gap:12px;font-size:27px;font-weight:700}

/* testimonial */
.testimonial{top:2535px;height:262px;background:var(--testimonial-bg);color:var(--white);text-align:center}
.testimonial blockquote{position:absolute;left:0;top:76px;width:100%;font-size:19px;font-style:italic;line-height:32px;font-weight:400}
.testimonial .name{position:absolute;left:0;top:162px;width:100%;font-size:13px;font-weight:600;letter-spacing:2px}
.dots{position:absolute;top:217px;left:0;width:100%;display:flex;justify-content:center;align-items:center;gap:10px}
.dots span{width:5px;height:5px;border-radius:50%;background:#bbbbbb}
.dots span.on{width:8px;height:8px;background:var(--white)}

/* footer */
.site-footer{top:2797px;height:205px;background:var(--footer-bg);color:var(--white)}
.footer-brand{position:absolute;left:85px;top:74px;font-size:25px;font-weight:700}
.copyright{position:absolute;left:85px;top:124px;font-size:13px;color:#cccccc}
.footer-links{position:absolute;top:75px;display:grid;grid-template-rows:repeat(4,32px);font-size:13px;font-weight:600;color:var(--footer-link)}
</style>
</head>
<body>

<header class="site-header">
  <a class="brand" href="#">GLOWVRA</a>
  <nav class="main-nav">
    <a class="active" href="#">HOME</a>
    <a href="#">ABOUT US</a>
    <a href="#">CONTACT</a>
    <a href="#">LOGIN</a>
  </nav>
  <a class="btn-started" href="#">GET STARTED</a>
</header>

<section class="section hero">
  <div class="photo" role="img" aria-label="Woman in a wide white sun hat with red lips, fashion portrait"></div>
  <h1 class="hero-title">Looking for a <em>Make Up</em><br>or <em>Facial Care</em> Service?</h1>
  <a class="btn-signin" href="#">SIGN IN</a>
  <svg class="slider-arrow" style="left:37px" width="16" height="34" viewBox="0 0 16 34"><polyline points="14,2 2,17 14,32" fill="none" stroke="#444" stroke-width="2"/></svg>
  <svg class="slider-arrow" style="left:1152px" width="16" height="34" viewBox="0 0 16 34"><polyline points="2,2 14,17 2,32" fill="none" stroke="#444" stroke-width="2"/></svg>
</section>

<section class="section feature esthetician">
  <div class="photo" role="img" aria-label="Close-up beauty portrait of a woman with glowing skin under red light"></div>
  <div class="copy">
    <h2>ARE YOU AN ESTHETICIAN?</h2>
    <p>Lorem ipsum dolor sit amet, eam ludus invidunt an, prompta<br>labores fuisset quo in. Paulo vocent fuisset eu vis,<br>nec malorum percipit ad Feugait deserunt.</p>
    <a class="more" href="#">JOIN OUR NETWORK <svg width="8" height="12" viewBox="0 0 8 12"><polyline points="1,1 6,6 1,11" fill="none" stroke="#fff" stroke-width="1.6"/></svg></a>
  </div>
</section>

<section class="section feature makeup">
  <div class="photo" role="img" aria-label="Beauty portrait of a woman with red and black winged eyeliner"></div>
  <div class="copy">
    <h2>LOOKING FOR A MAKE UP?</h2>
    <p>Lorem ipsum dolor sit amet, eam ludus invidunt an, prompta<br>labores fuisset quo in. Paulo vocent fuisset eu vis,<br>nec malorum percipit ad Feugait deserunt.</p>
    <a class="more" href="#">LEARN MORE <svg width="8" height="12" viewBox="0 0 8 12"><polyline points="1,1 6,6 1,11" fill="none" stroke="#fff" stroke-width="1.6"/></svg></a>
  </div>
</section>

<section class="section quote">
  <blockquote>“A girl should be two things: classy and fabulous.”</blockquote>
  <cite>- CORALIE VANCE</cite>
</section>

<section class="section about">
  <h2>ABOUT US</h2>
  <div class="about-col" style="left:87px">
    <h3>Our commitment</h3>
    <p>Lorem ipsum dolor sit amet, consectetur adipisicing elit, sed do eiusmod tempor incididunt ut labore et dolore magna aliqua. Ut enim ad minim veniam, quis nostrud exercitation ullamco laboris nisi ut aliquip ex ea commodo consequat.</p>
  </div>
  <div class="about-col" style="left:439px">
    <h3>Safety</h3>
    <p>Lorem ipsum dolor sit amet, consectetur adipisicing elit, sed do eiusmod tempor incididunt ut labore et dolore magna aliqua. Ut enim ad minim veniam, quis nostrud exercitation ullamco laboris nisi ut aliquip ex ea commodo consequat.</p>
  </div>
  <div class="about-col" style="left:795px">
    <h3>Great Support</h3>
    <p>Lorem ipsum dolor sit amet, consectetur adipisicing elit, sed do eiusmod tempor incididunt ut labore et dolore magna aliqua. Ut enim ad minim veniam, quis nostrud exercitation ullamco laboris nisi ut aliquip ex ea commodo consequat.</p>
  </div>
</section>

<section class="section cta">
  <div class="cta-card cta-red" style="left:0">
    <div class="photo" role="img" aria-label="Close-up of red lips and a hand with red nails on a red background"></div>
    <a href="#" style="left:87px">FIND MAKE UP ARTIST <svg width="28" height="24" viewBox="0 0 28 24"><path d="M2 12H25M15 2l10 10-10 10" fill="none" stroke="#fff" stroke-width="3.2"/></svg></a>
  </div>
  <div class="cta-card cta-blue" style="left:600px">
    <div class="photo" role="img" aria-label="Portrait of a woman with sleek dark hair on a pale blue background"></div>
    <a href="#" style="left:50px">JOIN OUR NETWORK <svg width="28" height="24" viewBox="0 0 28 24"><path d="M2 12H25M15 2l10 10-10 10" fill="none" stroke="#fff" stroke-width="3.2"/></svg></a>
  </div>
</section>

<section class="section testimonial">
  <blockquote>I have always found GLOWVRA service standard to be very high<br>with all staff being very knowledgeable and helpful.</blockquote>
  <div class="name">MARA QUELL</div>
  <div class="dots"><span class="on"></span><span></span><span></span></div>
</section>

<footer class="section site-footer">
  <div class="footer-brand">GLOWVRA</div>
  <div class="copyright">© 2019 GLOWVRA. All rights reserved.</div>
  <nav class="footer-links" style="left:845px">
    <a href="#">About US</a><a href="#">Support</a><a href="#">FAQ</a><a href="#">Lost &amp; Found</a>
  </nav>
  <nav class="footer-links" style="left:1004px">
    <a href="#">User Agreements</a><a href="#">Glowvra Street</a><a href="#">Tip Consultant</a><a href="#">Contact</a>
  </nav>
</footer>

</body>
</html>
```